HiItsJonBrell.com needs a modern, eye-catching business card design

My name is Jon Brell and I own a video training (software development industry) website. I need a business card design that is eye catching for when I travel to conferences or do seminars. I would prefer something simple but bold. Something along the lines of this: https://pixvaultstatic.example/gallery_img/530172/44018/44018_9917302_530172_image.jpg

Note that I do not have a specific logo, but I do have an caricature I use on my site of myself. I've not attached it because I'm not really a fan of having it on my business cards. I would prefer lettering instead of an image. You can go to my website (https://hiitsjonbrell.com) for inspiration.

I want to add the following information on my card (the order of these, their size, and their casing is up to you):

Jon Brell
jon@HiItsJonBrell.com
@HiItsJonBrell
HiItsJonBrell.com
vidsharehub.example/HiItsJonBrell

I would also like to have somewhere on the card a small ad that says "Get a free course at https://HiItsJonBrell.com/FreeCourse". Feel free to play with that wording or layout if you need. I would prefer this text to be at the bottom of the card and subtle. Some small eye-catching thing might be ok but nothing huge or garish.

I plan on printing this card at pressquill.example (https://www.pressquill.example/us/design-guidelines/business-cards.html). I would like it to be the standard size (3.66" x 2.16"). I would prefer rounded corners and horizontal orientation. This is a two-side design. I would prefer the side with all of the information be primarily white but I like color text (again, flexible on that). On the front side, I like simple. Maybe just HiItsJonBrell.com (casing on that is up to you - whatever looks and reads the best - that goes for all of the casing). As for font choices, I prefer a modern, clean font. For example, Open Sans Light can be a nice option.

Website Info (might be helpful for the card):
Color Palette

Darkest blue - #263246
Alternate blue - #2F4E6A
Light blue - #2A98C3
Orange - #FF6201
White - #FFFFFF

Font for Jon Brell Logo

Jellyka Estryas Handwriting
http://www.typecrate.example/jellyka_estryas_handwriting.font

Fonts for Site Content and VidShare Thumbnails

Lovelo (bold title font)
http://www.glyphmill.example/lovelo-font/

Open Sans (body font)
http://www.letterbarn.example/fonts/open-sans

Industry/Entity Type

Software Development

Contact Information for Business Card

Jon Brell
jon@HiItsJonBrell.com
@HiItsJonBrell
HiItsJonBrell.com
vidsharehub.example/HiItsJonBrell

Get a free course at https://HiItsJonBrell.com/FreeCourse

Colors

Designer to choose colors to be used in the design.

Requirements
Nice to have
• Modern color - maybe primarily a color on the front and then that color as an accent on the back.
Should not have
• Lots of colors - I LOVE color but do not want a rainbow of colors on the card.

```html
<!DOCTYPE html>
<html lang="en">
<head>
<meta charset="utf-8">
<title>Jon Brell — Business Card</title>
<link rel="stylesheet" href="https://fonts.googleapis.com/css2?family=Open+Sans:wght@300;400&display=swap">
<style>
  :root {
    --darkest-blue: #263246;
    --alt-blue: #2F4E6A;
    --light-blue: #2A98C3;
    --band-blue: #2289bb;
    --orange: #FF6201;
    --white: #FFFFFF;
    --paper: #f7f7f7;
    --backdrop: #d9dbde;
    --rule: #b9bcc0;
  }
  html, body {
    margin: 0;
    width: 1200px;
    height: 900px;
    overflow: hidden;
    background: var(--backdrop);
    font-family: "Open Sans", sans-serif;
  }
  .stage {
    position: relative;
    width: 1200px;
    height: 900px;
  }
  .card {
    position: absolute;
    left: 260px;
    width: 680px;
    height: 401px;
    border-radius: 18px;
    overflow: hidden;
    box-shadow: 0 6px 18px rgba(0,0,0,0.18);
  }
  .card--front {
    top: 36px;
    background: linear-gradient(160deg, #32a6d3 0%, var(--light-blue) 100%);
    display: flex;
    align-items: center;
    justify-content: center;
  }
  .front-url {
    color: var(--white);
    font-weight: 300;
    font-size: 40px;
    letter-spacing: 0.5px;
    opacity: 0.92;
  }
  .card--back {
    top: 463px;
    background: linear-gradient(180deg, var(--white) 0%, var(--paper) 100%);
  }
  .brand-name {
    position: absolute;
    left: 70px;
    top: 150px;
    margin: 0;
    font-weight: 300;
    font-size: 50px;
    color: var(--darkest-blue);
    letter-spacing: 0.5px;
  }
  .divider {
    position: absolute;
    left: 330px;
    top: 122px;
    width: 1px;
    height: 110px;
    background: var(--rule);
  }
  .contact-list {
    position: absolute;
    left: 352px;
    top: 120px;
    margin: 0;
    padding: 0;
    list-style: none;
  }
  .contact-item {
    display: flex;
    align-items: center;
    gap: 9px;
    height: 28px;
    font-size: 14.5px;
    font-weight: 400;
    color: var(--darkest-blue);
  }
  .contact-icon {
    width: 18px;
    height: 18px;
    flex: none;
  }
  .promo-band {
    position: absolute;
    left: 0;
    right: 0;
    top: 300px;
    height: 44px;
    background: var(--band-blue);
    display: flex;
    align-items: center;
    padding-left: 150px;
    color: var(--white);
    font-size: 17px;
    font-weight: 400;
  }
</style>
</head>
<body>
<main class="stage">
  <section class="card card--front" aria-label="Card front">
    <span class="front-url">HiItsJonBrell.com</span>
  </section>

  <section class="card card--back" aria-label="Card back">
    <h1 class="brand-name">Jon Brell</h1>
    <div class="divider"></div>
    <ul class="contact-list">
      <li class="contact-item">
        <svg class="contact-icon" viewBox="0 0 18 18" aria-hidden="true"><circle cx="9" cy="9" r="9" fill="var(--light-blue)"/></svg>
        @HiItsJonBrell
      </li>
      <li class="contact-item">
        <svg class="contact-icon" viewBox="0 0 18 18" aria-hidden="true">
          <circle cx="9" cy="9" r="9" fill="var(--alt-blue)"/>
          <rect x="4.5" y="6" width="9" height="6.5" fill="none" stroke="var(--white)" stroke-width="1.2"/>
          <path d="M4.5 6 L9 9.8 L13.5 6" fill="none" stroke="var(--white)" stroke-width="1.2"/>
        </svg>
        jon@HiItsJonBrell.com
      </li>
      <li class="contact-item">
        <svg class="contact-icon" viewBox="0 0 18 18" aria-hidden="true">
          <circle cx="9" cy="9" r="9" fill="var(--darkest-blue)"/>
          <circle cx="9" cy="9" r="4.6" fill="none" stroke="var(--white)" stroke-width="1.1"/>
          <ellipse cx="9" cy="9" rx="2" ry="4.6" fill="none" stroke="var(--white)" stroke-width="1"/>
          <line x1="4.4" y1="9" x2="13.6" y2="9" stroke="var(--white)" stroke-width="1"/>
        </svg>
        www.HiItsJonBrell.com
      </li>
      <li class="contact-item">
        <svg class="contact-icon" viewBox="0 0 18 18" aria-hidden="true"><circle cx="9" cy="9" r="9" fill="var(--orange)"/></svg>
        vidsharehub.example/HiItsJonBrell
      </li>
    </ul>
    <div class="promo-band">Get a free course at https://HiItsJonBrell.com/FreeCourse</div>
  </section>
</main>
</body>
</html>
```